Melko's Pizzeria Direct Mail Postcard

Looking for a direct mail postcard with a similar design as the one attached, with our logo and store information. This has to meet qdrn direct mail standards and have the postage block printed on the back of cards. I will send over text edits once we get the design we like. The back of the card can have store info and coupons, just have to make sure the coupons on the back dont match the same space as coupons on the front so customers can cut them out. Please use the attached card as a guide. I want to have the same basic design

Industry/Entity Type

Pizza Delivery

Colors

Designer to choose colors to be used in the design.

Requirements
Must have
• QDRN Direct Mail capability
Nice to have
• Great pictures

```html
<!DOCTYPE html>
<html lang="en">
<head>
<meta charset="utf-8">
<title>Melko's Pizzeria Direct Mail Postcard</title>
<link rel="stylesheet" href="https://fonts.googleapis.com/css2?family=Lato:wght@300;400;700;900&family=Open+Sans:wght@400;600&family=Roboto+Condensed:wght@400;700&family=Arimo:wght@400;700&display=swap">
<style>
  :root {
    --page: #e9e4dc;
    --brick: #4b4b4d;
    --brick-dark: #2f2f31;
    --ink-black: #1c1c1c;
    --red: #d71f26;
    --red-deep: #a8141a;
    --tan: #a97c45;
    --tan-dark: #3a2a18;
    --white: #ffffff;
    --paper: #fbfbfb;
    --text-dark: #222222;
    --crust: #d99a4e;
    --sauce: #b8341f;
  }
  * { box-sizing: border-box; margin: 0; padding: 0; }
  html, body { width: 1200px; height: 1200px; overflow: hidden; background: var(--page); }
  .canvas { position: relative; width: 1200px; height: 1200px; }
  .postcard {
    position: absolute; width: 804px; height: 520px; overflow: hidden;
    box-shadow: 0 4px 14px rgba(0,0,0,.25);
  }

  /* Front */
  .postcard--front {
    left: 52px; top: 50px;
    background: linear-gradient(180deg, var(--brick) 0%, #3d3d3f 60%, var(--brick-dark) 100%);
    font-family: "Open Sans", sans-serif;
  }
  .front-art { position: absolute; inset: 0; }
  .brand {
    position: absolute; left: 580px; top: 130px; width: 170px;
    display: flex; align-items: center; gap: 8px;
  }
  .brand__dot { width: 22px; height: 22px; border-radius: 50%; background: var(--red); flex: none; }
  .brand__name {
    font-family: "Open Sans", sans-serif; font-weight: 600; font-size: 20px;
    color: var(--white); line-height: 1.1;
  }
  .coupon-frame {
    position: absolute; border: 2px dashed rgba(255,255,255,.85); border-radius: 8px;
  }
  .coupon-frame--large { left: 456px; top: 250px; width: 298px; height: 118px; }
  .coupon-frame--small { left: 552px; top: 385px; width: 202px; height: 78px; }
  .coupon-card {
    position: absolute; background: var(--white); border-radius: 6px;
    display: flex;
  }
  .coupon-frame--large .coupon-card { left: 8px; top: 9px; right: 8px; bottom: 9px; padding: 10px 12px; }
  .coupon-frame--small .coupon-card { left: 5px; top: 5px; right: 5px; bottom: 5px; padding: 6px 8px; }
  .deal { flex: 1; }
  .deal + .deal { border-left: 1.5px solid #333; padding-left: 12px; margin-left: 4px; }
  .coupon-frame--small .deal + .deal { padding-left: 9px; }
  .deal__price {
    font-family: "Roboto Condensed", sans-serif; color: var(--red);
    font-size: 29px; line-height: 1; margin-bottom: 6px;
  }
  .deal__copy { font-size: 9px; line-height: 1.25; color: var(--text-dark); }
  .coupon-frame--small .deal__price { font-size: 19px; margin-bottom: 4px; }
  .coupon-frame--small .deal__copy { font-size: 6px; }
  .front-copy {
    position: absolute; left: 26px; top: 345px; width: 408px;
    color: var(--white); font-weight: 600; font-size: 12.4px; line-height: 1.25;
    text-align: justify;
  }
  .front-copy p + p { margin-top: 8px; }
  .front-band {
    position: absolute; left: 0; right: 0; bottom: 0; height: 26px;
    background: linear-gradient(180deg, var(--red) 0%, var(--red-deep) 70%, #5e1a1a 100%);
  }

  /* Back */
  .postcard--back {
    left: 308px; top: 616px; background: var(--paper);
    font-family: "Lato", sans-serif;
  }
  .back-art { position: absolute; inset: 0; }
  .stamp-coupon { position: absolute; }
  .stamp-coupon svg { position: absolute; inset: 0; }
  .stamp-coupon--tan { left: 38px; top: 30px; width: 244px; height: 134px; }
  .stamp-coupon--red { left: 62px; top: 184px; width: 196px; height: 108px; }
  .stamp-coupon__body { position: absolute; inset: 0; display: flex; align-items: center; }
  .stamp-coupon__rate { position: relative; text-align: center; }
  .rate__num { font-family: "Roboto Condensed", sans-serif; color: var(--white); line-height: .9; }
  .rate__unit { position: absolute; color: var(--white); font-weight: 400; line-height: .9; text-align: left; }
  .stamp-coupon__label { line-height: 1; }
  .label__top { font-weight: 700; }
  .label__mid { font-weight: 300; letter-spacing: 1px; }

  .stamp-coupon--tan .stamp-coupon__rate { margin-left: 22px; width: 130px; }
  .stamp-coupon--tan .rate__num { font-size: 62px; padding-right: 46px; }
  .stamp-coupon--tan .rate__unit { left: 72px; top: 2px; font-size: 24px; }
  .stamp-coupon--tan .rate__caption { font-size: 14px; color: var(--tan-dark); margin-top: 6px; padding-right: 10px; }
  .stamp-coupon--tan .stamp-coupon__label { margin-left: 2px; color: var(--tan-dark); }
  .stamp-coupon--tan .label__top { font-size: 24px; }
  .stamp-coupon--tan .label__mid { font-size: 27px; color: var(--white); margin: 2px 0 8px; }
  .stamp-coupon--tan .label__sub { font-size: 14px; }

  .stamp-coupon--red .stamp-coupon__rate { margin-left: 20px; width: 100px; }
  .stamp-coupon--red .rate__num { font-size: 48px; padding-right: 36px; }
  .stamp-coupon--red .rate__unit { left: 56px; top: 2px; font-size: 19px; }
  .stamp-coupon--red .rate__caption { font-size: 11px; color: var(--ink-black); margin-top: 6px; padding-right: 6px; }
  .stamp-coupon--red .stamp-coupon__label { color: var(--ink-black); }
  .stamp-coupon--red .label__top { font-size: 19px; }
  .stamp-coupon--red .label__mid { font-size: 21px; color: var(--white); margin: 2px 0 6px; }
  .stamp-coupon--red .label__sub { font-size: 11px; }

  .back-copy {
    position: absolute; left: 26px; top: 324px; width: 306px;
    color: var(--white); font-size: 9.6px; line-height: 1.3; text-align: justify;
  }
  .back-copy__edge {
    float: right; width: 40px; height: 150px;
    shape-outside: polygon(40px 0, 40px 30px, 6px 150px, 40px 150px);
  }
  .back-copy p + p { margin-top: 10px; }
  .back-copy__tagline {
    position: absolute; left: 32px; top: 468px;
    color: var(--red); font-weight: 700; font-size: 14.5px;
  }
  .indicia {
    position: absolute; left: 649px; top: 30px; width: 116px; height: 88px;
    border: 1px solid var(--ink-black); background: var(--white);
    font-family: "Arimo", sans-serif; font-size: 13px; line-height: 1.22;
    text-align: center; color: var(--ink-black); padding-top: 4px;
  }
  .indicia strong { font-size: 14.5px; }
  .address-block {
    position: absolute; left: 525px; top: 164px; width: 235px; height: 87px;
    border: 1.5px solid var(--ink-black); background: var(--white);
    font-family: "Arimo", sans-serif; color: var(--ink-black);
    padding: 7px 0 0 16px;
  }
  .address-block__route { font-size: 12px; letter-spacing: -.2px; }
  .address-block__lines { font-size: 13.5px; line-height: 1.25; margin-top: 22px; }
</style>
</head>
<body>
<main class="canvas">

  <section class="postcard postcard--front">
    <svg class="front-art" width="804" height="520" viewBox="0 0 804 520">
      <defs>
        <radialGradient id="pizzaMain" cx="50%" cy="50%" r="50%">
          <stop offset="0%" stop-color="#c9463a"/>
          <stop offset="60%" stop-color="#b8341f"/>
          <stop offset="90%" stop-color="#d58a4a"/>
          <stop offset="100%" stop-color="#d99a4e"/>
        </radialGradient>
        <radialGradient id="pizzaTop" cx="50%" cy="40%" r="55%">
          <stop offset="0%" stop-color="#c7331f"/>
          <stop offset="80%" stop-color="#b3301f"/>
          <stop offset="100%" stop-color="#d99a4e"/>
        </radialGradient>
        <radialGradient id="tomatoGlow" cx="50%" cy="50%" r="50%">
          <stop offset="0%" stop-color="#c2561f" stop-opacity=".45"/>
          <stop offset="100%" stop-color="#c2561f" stop-opacity="0"/>
        </radialGradient>
      </defs>
      <circle cx="780" cy="130" r="60" fill="url(#tomatoGlow)"/>
      <circle cx="560" cy="480" r="70" fill="url(#tomatoGlow)"/>
      <g role="img" aria-label="Photo of a sliced pepperoni and pepper pizza">
        <circle cx="120" cy="170" r="215" fill="url(#pizzaMain)"/>
      </g>
      <g role="img" aria-label="Photo of a tomato and herb pizza">
        <ellipse cx="458" cy="0" rx="152" ry="130" fill="url(#pizzaTop)"/>
      </g>
    </svg>

    <div class="brand">
      <span class="brand__dot"></span>
      <span class="brand__name">Melko's Pizzeria</span>
    </div>

    <div class="coupon-frame coupon-frame--large">
      <div class="coupon-card">
        <div class="deal">
          <p class="deal__price">$6.00 off</p>
          <p class="deal__copy">Lorem Ipsum is simply dummy text of the printing and typesetting industry</p>
        </div>
        <div class="deal">
          <p class="deal__price">$5.00 off</p>
          <p class="deal__copy">Lorem Ipsum is simply dummy text of the printing and typesetting industry</p>
        </div>
      </div>
    </div>

    <div class="coupon-frame coupon-frame--small">
      <div class="coupon-card">
        <div class="deal">
          <p class="deal__price">$2.00 off</p>
          <p class="deal__copy">Lorem Ipsum is simply dummy text of the printing and typesetting industry</p>
        </div>
        <div class="deal">
          <p class="deal__price">$2.00 off</p>
          <p class="deal__copy">Lorem Ipsum is simply dummy text of the printing and typesetting industry</p>
        </div>
      </div>
    </div>

    <div class="front-copy">
      <p>Lorem Ipsum is simply dummy text of the printing and typesetting industry. Lorem Ipsum has been the industry's standard dummy text ever since the 1500s, when an unknown printer took a galley of type and scrambled it to make a type specimen book.</p>
      <p>Lorem Ipsum is simply dummy text of the printing and typesetting industry. Lorem Ipsum has been the industry's standard dummy text ever since the 1500s, when an unknown printer took a galley of type and scrambled it to make a type specimen book.</p>
    </div>

    <div class="front-band"></div>
  </section>

  <section class="postcard postcard--back">
    <svg class="back-art" width="804" height="520" viewBox="0 0 804 520">
      <defs>
        <radialGradient id="pizzaFaint" cx="55%" cy="60%" r="55%">
          <stop offset="0%" stop-color="#d9b49a" stop-opacity=".45"/>
          <stop offset="100%" stop-color="#f3ece6" stop-opacity="0"/>
        </radialGradient>
        <linearGradient id="brickDark" x1="0" y1="0" x2="0" y2="1">
          <stop offset="0%" stop-color="#262628"/>
          <stop offset="100%" stop-color="#1c1c1c"/>
        </linearGradient>
      </defs>
      <g role="img" aria-label="Faded photo of a pepperoni pizza">
        <rect x="380" y="260" width="424" height="260" fill="url(#pizzaFaint)"/>
      </g>
      <polygon points="0,0 424,0 304,520 0,520" fill="url(#brickDark)"/>
      <polygon points="424,0 458,0 348,356" fill="#d71f26"/>
    </svg>

    <div class="stamp-coupon stamp-coupon--tan">
      <svg width="244" height="134" viewBox="0 0 244 134">
        <rect x="0" y="0" width="244" height="134" rx="4" fill="#a97c45"/>
        <rect x="1.5" y="1.5" width="241" height="131" fill="none" stroke="#2a2a2a" stroke-width="3" stroke-dasharray="6 6"/>
      </svg>
      <div class="stamp-coupon__body">
        <div class="stamp-coupon__rate">
          <div class="rate__num">00</div>
          <div class="rate__unit">%<br>off</div>
          <div class="rate__caption">Lorem Ipsum</div>
        </div>
        <div class="stamp-coupon__label">
          <div class="label__top">LOREM</div>
          <div class="label__mid">IPSUM</div>
          <div class="label__sub">Lorem Ipsum</div>
        </div>
      </div>
    </div>

    <div class="stamp-coupon stamp-coupon--red">
      <svg width="196" height="108" viewBox="0 0 196 108">
        <rect x="0" y="0" width="196" height="108" rx="4" fill="#d71f26"/>
        <rect x="1.5" y="1.5" width="193" height="105" fill="none" stroke="#2a2a2a" stroke-width="3" stroke-dasharray="5 5"/>
      </svg>
      <div class="stamp-coupon__body">
        <div class="stamp-coupon__rate">
          <div class="rate__num">00</div>
          <div class="rate__unit">%<br>off</div>
          <div class="rate__caption">Lorem Ipsum</div>
        </div>
        <div class="stamp-coupon__label">
          <div class="label__top">LOREM</div>
          <div class="label__mid">IPSUM</div>
          <div class="label__sub">Lorem Ipsum</div>
        </div>
      </div>
    </div>

    <div class="back-copy">
      <span class="back-copy__edge"></span>
      <p>Lorem Ipsum is simply dummy text of the printing and typesetting industry. Lorem Ipsum has been the industry's standard dummy text ever since the 1500s, when an unknown printer took a galley of type and scrambled it to make a type specimen book.</p>
      <p>It has survived not only five centuries, but also the leap into electronic typesetting, remaining essentially unchanged. It was popularised in the 1960s with the release of Tyrell sheets containing Lorem Ipsum passages, and more recently with desktop publishing software like Folio Layout including versions of Lorem Ipsum.</p>
    </div>
    <p class="back-copy__tagline">Lorem Ipsum is simply dummy text</p>

    <div class="indicia">
      PRSRT STD<br>ECRWSS<br>QDRN POSTAGE<br><strong>PAID</strong><br>QDRN Retail
    </div>

    <div class="address-block">
      <p class="address-block__route">****************ECRWSSQDRN****</p>
      <p class="address-block__lines">Postal Customer<br>City, State, 5-Digit ZIP Code</p>
    </div>
  </section>

</main>
</body>
</html>
```